Corvell Bookkeeping Services business cards

looking for a double sided business card design. My logo is attached. I am looking for a design similar to the attached. Keen to see what my logo in white on the blue background would look like.

```html
<!DOCTYPE html>
<html lang="en">
<head>
<meta charset="utf-8">
<title>Corvell Bookkeeping Services – Business Cards</title>
<link rel="stylesheet" href="https://fonts.googleapis.com/css2?family=Poppins:wght@400;500;700;800&display=swap">
<style>
  :root {
    --navy: #0b2f63;
    --navy-deep: #073468;
    --green: #93b62b;
    --green-bright: #9cbd2c;
    --card-white: #ffffff;
    --backdrop: #dcdcdd;
    --shadow: rgba(0, 0, 0, 0.18);
  }
  * { box-sizing: border-box; margin: 0; padding: 0; }
  html, body {
    width: 1200px; height: 750px; overflow: hidden;
    background: var(--backdrop);
    font-family: "Poppins", sans-serif;
  }
  .canvas { position: relative; width: 1200px; height: 750px; }

  .card {
    position: absolute;
    width: 560px; height: 320px;
    border-radius: 26px;
    box-shadow: 0 10px 24px var(--shadow);
    overflow: hidden;
  }

  /* Front */
  .card--front {
    left: 60px; top: 70px;
    background: linear-gradient(115deg, var(--navy-deep) 0%, #1b5560 40%, #5f8a43 70%, var(--green-bright) 100%);
    display: flex; align-items: center; justify-content: center;
  }
  .front-wordmark {
    display: flex; align-items: center; gap: 18px;
    color: var(--card-white);
    font-weight: 800;
  }
  .front-wordmark__mark {
    width: 54px; height: 54px; background: var(--card-white); border-radius: 4px;
  }
  .front-wordmark__name { font-size: 46px; line-height: 1; letter-spacing: -0.5px; }
  .front-wordmark__tag { font-size: 14.5px; letter-spacing: 2.2px; margin-top: 6px; }

  /* Back */
  .card--back {
    left: 580px; top: 360px;
    background: var(--card-white);
    padding: 34px 36px;
  }
  .back-wordmark { color: var(--navy); font-weight: 800; }
  .back-wordmark__name { font-size: 40px; line-height: 1; letter-spacing: -0.5px; }
  .back-wordmark__tag { font-size: 12px; letter-spacing: 2px; margin-top: 5px; }

  .contact-person { margin-top: 26px; }
  .contact-person__name { color: var(--green); font-weight: 700; font-size: 22px; line-height: 1.1; }
  .contact-person__role { color: var(--navy); font-size: 13px; margin-top: 2px; }

  .contact-list { list-style: none; margin-top: 12px; color: var(--navy); font-size: 13px; }
  .contact-list li { display: flex; align-items: center; gap: 8px; line-height: 1.65; }
  .contact-list svg { width: 11px; height: 11px; fill: var(--green); flex: none; }
  .contact-list .abn-label { color: var(--green); font-weight: 700; }

  .postal-address {
    position: absolute; right: 36px; bottom: 36px;
    text-align: right; color: var(--navy); font-size: 12.5px; line-height: 1.5;
  }
</style>
</head>
<body>
<main class="canvas">

  <section class="card card--front" aria-label="Card front">
    <div class="front-wordmark">
      <span class="front-wordmark__mark"></span>
      <div>
        <div class="front-wordmark__name">Corvell</div>
        <div class="front-wordmark__tag">BOOKKEEPING SERVICES</div>
      </div>
    </div>
  </section>

  <section class="card card--back" aria-label="Card back">
    <div class="back-wordmark">
      <div class="back-wordmark__name">Corvell</div>
      <div class="back-wordmark__tag">BOOKKEEPING SERVICES</div>
    </div>

    <div class="contact-person">
      <div class="contact-person__name">Daniel Hartley</div>
      <div class="contact-person__role">Founder &amp; Bookkeeping Expert</div>
    </div>

    <ul class="contact-list">
      <li>
        <svg viewBox="0 0 24 24" aria-hidden="true"><path d="M6.6 10.8a15 15 0 0 0 6.6 6.6l2.2-2.2a1 1 0 0 1 1-.25 11.4 11.4 0 0 0 3.6.57 1 1 0 0 1 1 1V20a1 1 0 0 1-1 1A17 17 0 0 1 3 4a1 1 0 0 1 1-1h3.5a1 1 0 0 1 1 1c0 1.25.2 2.45.57 3.57a1 1 0 0 1-.25 1z"/></svg>
        0412 386 204
      </li>
      <li>
        <svg viewBox="0 0 24 24" aria-hidden="true"><path d="M2 5h20v14H2z M2 5l10 8 10-8" fill="none" stroke="#93b62b" stroke-width="2.4"/></svg>
        hello@corvellbookkeeping.com.au
      </li>
      <li>
        <svg viewBox="0 0 24 24" aria-hidden="true"><circle cx="12" cy="12" r="9.5" fill="none" stroke="#93b62b" stroke-width="2.4"/><path d="M2.5 12h19M12 2.5c3 3 3 16 0 19M12 2.5c-3 3-3 16 0 19" fill="none" stroke="#93b62b" stroke-width="2"/></svg>
        corvellbookkeeping.com.au
      </li>
      <li><span class="abn-label">ABN:</span> 63 118 402 957</li>
    </ul>

    <address class="postal-address" style="font-style: normal;">
      PO Box 3412, Marlow<br>Queensland 4310
    </address>
  </section>

</main>
</body>
</html>
```